Corvel Networks Marketing Website

Corvel Networks is the brand for a series of nation-wide internet peering exchanges operated by the Southern Coastal Data Collective Inc. (SCDC), a not-for-profit association founded in 1995.

Our current website is built on Drupal, and we are looking to migrate to WordPress with a similarly clean and modern theme:

http://www.corvelnet.example/

Target Market(s)

Technical and professional staff from the telecommunications industry in Australia.

Industry/Entity Type

Telecom

Font styles to use
Sans Serif

Requirements
Must have
• Responsive layout for mobile viewers
• Compatible with WordPress 4.2.2 and PHP 5.5.
• Winning entry will provide a completed WordPress theme file compatible .
• Usage of the "Corvel Networks" logo must comply with the attached style guide.

```html
<!DOCTYPE html>
<html lang="en">
<head>
<meta charset="utf-8">
<title>Corvel Networks — Internet Peering for Australia</title>
<link rel="stylesheet" href="https://fonts.googleapis.com/css2?family=Open+Sans:wght@400;600;700&display=swap">
<style>
:root{
  --brand:#5877b9;
  --brand-dark:#4a69aa;
  --brand-link:#3f63a8;
  --ink:#333333;
  --muted:#777777;
  --nav:#444444;
  --light-band:#ececec;
  --white:#ffffff;
  --hero-top:#3d5a70;
  --hero-mid:#5f7d8d;
  --hero-low:#1f3442;
  --org-a:#1b2128;
  --org-b:#3a4650;
}
*{box-sizing:border-box;margin:0;padding:0}
html,body{width:1200px;height:2539px;overflow:hidden}
body{position:relative;font-family:"Open Sans",Arial,sans-serif;color:var(--ink);background:var(--white)}
.abs{position:absolute}

/* header */
.site-header{left:0;top:0;width:1200px;height:78px;background:var(--white)}
.brand{display:flex;align-items:center;gap:10px;font-weight:700;color:var(--brand);font-size:22px;letter-spacing:.5px}
.brand-mark{width:20px;height:20px;background:var(--brand)}
.site-header .brand{position:absolute;left:98px;top:24px}
.main-nav{position:absolute;top:31px;left:0;width:1200px;font-size:13px;color:var(--nav);text-transform:uppercase}
.main-nav span{position:absolute}

/* hero */
.hero{left:0;top:78px;width:1200px;height:502px;background:linear-gradient(180deg,var(--hero-top) 0%,var(--hero-mid) 40%,var(--hero-low) 100%)}
.hero-arrow{width:34px;height:34px;border-radius:50%;background:rgba(255,255,255,.25);top:224px}
.hero-title{left:500px;top:276px;font-size:32px;font-weight:700;color:var(--white)}
.hero-sub{left:502px;top:322px;font-size:19px;color:var(--white)}
.btn{display:flex;align-items:center;justify-content:center;background:var(--brand);color:var(--white);font-size:15px;border-radius:2px}
.hero .btn{position:absolute;left:504px;top:370px;width:153px;height:44px}

/* what we do */
.section-title{font-size:26px;font-weight:700;color:var(--ink);text-align:center;width:1200px;left:0}
.icon-box{width:61px;height:61px;background:var(--brand);display:flex;align-items:center;justify-content:center}
.feature h3{font-size:13.5px;font-weight:700;color:var(--ink);text-transform:uppercase;margin-bottom:12px}
.feature p{font-size:11.5px;line-height:22px;color:var(--muted)}

/* organisation */
.org-band{left:0;top:953px;width:1200px;height:296px;background:linear-gradient(90deg,var(--org-a),var(--org-b) 50%,var(--org-a))}
.org-title{left:0;width:1200px;top:60px;text-align:center;font-size:24px;font-weight:700;color:var(--white)}
.org-text{left:0;width:1200px;top:106px;text-align:center;font-size:14px;line-height:24px;color:var(--white)}
.org-band .btn{position:absolute;left:506px;top:181px;width:190px;height:51px}

.scroll-down{left:573px;top:1619px;width:56px;height:56px;border-radius:50%;background:#eeeeee;border:1px solid #dddddd}

/* posts */
.posts{left:0;top:1735px;width:1200px;height:386px;background:var(--light-band)}
.posts h2{position:absolute;left:98px;top:56px;font-size:26px;font-weight:700;color:var(--ink)}
.post{position:absolute;top:112px;width:228px}
.post-thumb{width:228px;height:164px}
.post h3{margin-top:18px;font-size:13px;font-weight:700;color:var(--brand-link);text-transform:uppercase}
.post time{display:block;margin-top:8px;font-size:11px;color:var(--muted)}

/* partners */
.partners{left:0;top:2121px;width:1200px;height:123px;background:var(--white)}
.partner-badge{position:absolute;top:10px;width:138px;height:100px;background:#f3f3f3}
.partner-badge i{position:absolute;left:29px;top:38px;width:80px;height:24px;background:#c9c9c9;border-radius:3px}

/* footer */
.site-footer{left:0;top:2244px;width:1200px;height:232px;background:var(--brand);color:var(--white);text-align:center}
.site-footer h4{position:absolute;left:0;width:1200px;top:48px;font-size:16px;font-weight:700}
.site-footer .address{position:absolute;left:0;width:1200px;top:84px;font-size:14px}
.contact-line{position:absolute;left:0;width:1200px;top:122px;display:flex;justify-content:center;gap:34px;font-size:14px}
.contact-line span{display:flex;align-items:center;gap:8px}
.social{position:absolute;left:0;width:1200px;top:170px;display:flex;justify-content:center;gap:26px}
.social i{width:8px;height:8px;border-radius:50%;background:var(--white)}

.bottom-bar{left:0;top:2476px;width:1200px;height:63px;background:var(--brand-dark);color:var(--white)}
.bottom-bar .brand{position:absolute;left:98px;top:20px;color:var(--white);font-size:20px}
.bottom-bar .brand-mark{background:var(--white)}
.copyright{position:absolute;right:88px;top:24px;font-size:12px}
</style>
</head>
<body>

<header class="site-header abs">
  <div class="brand"><span class="brand-mark"></span>Corvel Networks</div>
  <nav class="main-nav">
    <span style="left:540px">Home</span>
    <span style="left:650px">Services</span>
    <span style="left:777px">Organisation</span>
    <span style="left:939px">Blog</span>
    <span style="left:1046px">Contact</span>
  </nav>
</header>

<section class="hero abs" role="img" aria-label="Photograph of a harbour city skyline with an opera house on the waterfront under a cloudy sky">
  <div class="hero-arrow abs" style="left:14px"></div>
  <div class="hero-arrow abs" style="left:1152px"></div>
  <h1 class="hero-title abs">NOT-FOR-PROFIT</h1>
  <p class="hero-sub abs">Australia's only not-for-profit and independent internet peering exchanges.</p>
  <a class="btn">Read More Info</a>
</section>

<h2 class="section-title abs" style="top:657px">WHAT WE DO</h2>

<div class="feature abs" style="left:98px;top:735px;width:310px;display:flex;gap:23px">
  <div class="icon-box"><svg width="28" height="28" viewBox="0 0 28 28"><circle cx="14" cy="9" r="6" fill="#fff"/><path d="M3 26c0-7 5-10 11-10s11 3 11 10z" fill="#fff"/></svg></div>
  <div><h3>Member Owned</h3><p>Corvel Networks is owned and operated by the Southern Coastal Data Collective Inc., meaning we are owned and run by our members. To get involved please email</p></div>
</div>
<div class="feature abs" style="left:450px;top:735px;width:310px;display:flex;gap:23px">
  <div class="icon-box"><svg width="24" height="30" viewBox="0 0 24 30"><rect x="2" y="1" width="20" height="28" fill="none" stroke="#fff" stroke-width="2.5"/><g fill="#fff"><rect x="6" y="5" width="4" height="4"/><rect x="14" y="5" width="4" height="4"/><rect x="6" y="12" width="4" height="4"/><rect x="14" y="12" width="4" height="4"/><rect x="6" y="19" width="4" height="4"/><rect x="14" y="19" width="4" height="4"/></g></svg></div>
  <div><h3>Commercially Neutral</h3><p>Not only are we Carrier Neutral but here at Corvel Networks we are also commercially neutral, this means anyone can peer provided you meet the technical requirements to do so.</p></div>
</div>
<div class="feature abs" style="left:793px;top:735px;width:320px;display:flex;gap:23px">
  <div class="icon-box"><svg width="30" height="26" viewBox="0 0 30 26"><path d="M3 6l8 3 8 3 6-6 4 2-5 6-6 6-8 5 2-6-4-5z" fill="#fff"/></svg></div>
  <div><h3>Australia Wide</h3><p>At Corvel Networks we are proud to operate 5 Peering Points throughout Australia. With a presence in 20 data centres across the nation we are bound to be at a data centre near you.</p></div>
</div>

<section class="org-band abs" role="img" aria-label="Photograph of a person standing in a long data centre aisle between server racks">
  <h2 class="org-title abs">ORGANISATION</h2>
  <p class="org-text abs">We are the country's only not-for-profit and independent internet peering provider. Member owned, carrier neutral,<br>with proven high quality peering services since 1997.</p>
  <a class="btn">Read More Info</a>
</section>

<div class="feature abs" style="left:98px;top:1330px;width:460px;display:flex;gap:24px">
  <div class="icon-box"><svg width="28" height="28" viewBox="0 0 28 28"><circle cx="14" cy="14" r="12" fill="#fff"/><path d="M9 7l5 2-1 5 4 3-2 5-4-4-3-4z" fill="var(--brand)"/></svg></div>
  <div><h3>Peering Points Across The Nation</h3><p>At Corvel Networks we have developed a robust peering fabric providing points of interconnect at most major data centres in Australia. This allows our members to participate in services, such as peering, where it is most beneficial for their network.</p></div>
</div>
<div class="feature abs" style="left:630px;top:1330px;width:470px;display:flex;gap:24px">
  <div class="icon-box"><svg width="28" height="24" viewBox="0 0 28 24"><g fill="#fff"><rect x="1" y="2" width="4" height="4"/><rect x="8" y="2" width="19" height="4"/><rect x="1" y="10" width="4" height="4"/><rect x="8" y="10" width="19" height="4"/><rect x="1" y="18" width="4" height="4"/><rect x="8" y="18" width="19" height="4"/></g></svg></div>
  <div><h3>Multilateral Peering Points</h3><p>Here at Corvel Networks we operate an extensive multilateral peering network with points of presence in most states of Australia.</p></div>
</div>
<div class="feature abs" style="left:98px;top:1489px;width:460px;display:flex;gap:24px">
  <div class="icon-box"><svg width="28" height="28" viewBox="0 0 28 28"><circle cx="14" cy="14" r="9" fill="none" stroke="#fff" stroke-width="5" stroke-dasharray="4 3"/><circle cx="14" cy="14" r="4" fill="#fff"/></svg></div>
  <div><h3>Member Owned &amp; Driven</h3><p>Being member based our focus is always on offering the best level of service and benefits for members and not on profits; services offered and further developed take direction from member requirements.</p></div>
</div>
<div class="feature abs" style="left:630px;top:1489px;width:470px;display:flex;gap:24px">
  <div class="icon-box"><svg width="28" height="28" viewBox="0 0 28 28"><path d="M6 24L22 6" stroke="#fff" stroke-width="2.5"/><ellipse cx="18" cy="14" rx="6" ry="3" fill="#fff" transform="rotate(-30 18 14)"/><ellipse cx="12" cy="10" rx="6" ry="3" fill="#fff" transform="rotate(-70 12 10)"/></svg></div>
  <div><h3>Not-For-Profit</h3><p>Corvel Networks is owned and operated by SCDC, a member based, not-for-profit association. All money is reinvested into services for members and stays within the association.</p></div>
</div>

<div class="scroll-down abs"><svg width="56" height="56" viewBox="0 0 56 56"><path d="M18 24l10 9 10-9" fill="none" stroke="#bbbbbb" stroke-width="2"/></svg></div>

<section class="posts abs">
  <h2>RECENT POSTS</h2>
  <article class="post" style="left:98px">
    <div class="post-thumb" role="img" aria-label="Photograph of network cables plugged into a switch" style="background:linear-gradient(160deg,#5a86c6,#2b4f88)"></div>
    <h3>EAST-HUB Peering Update</h3><time>Posted on Mar 31, 2015</time>
  </article>
  <article class="post" style="left:356px">
    <div class="post-thumb" role="img" aria-label="Photograph of a businessman touching a network diagram" style="background:linear-gradient(160deg,#3f6fa8,#0f2a4c)"></div>
    <h3>Peer Update</h3><time>Posted on Mar 31, 2015</time>
  </article>
  <article class="post" style="left:614px">
    <div class="post-thumb" role="img" aria-label="Photograph of server racks with status lights" style="background:linear-gradient(160deg,#24304a,#4a6b9e)"></div>
    <h3>110 Unique Peers!</h3><time>Posted on Mar 31, 2015</time>
  </article>
  <article class="post" style="left:872px">
    <div class="post-thumb" role="img" aria-label="Photograph of a man facing a wall of chalk arrows" style="background:linear-gradient(160deg,#6a6a6a,#3c3c3c)"></div>
    <h3>New POPs New Peers!</h3><time>Posted on Mar 31, 2015</time>
  </article>
</section>

<section class="partners abs" aria-label="Peering partners">
  <div class="partner-badge" style="left:92px"><i></i></div>
  <div class="partner-badge" style="left:270px"><i></i></div>
  <div class="partner-badge" style="left:432px"><i></i></div>
  <div class="partner-badge" style="left:612px"><i></i></div>
  <div class="partner-badge" style="left:782px"><i></i></div>
  <div class="partner-badge" style="left:950px"><i></i></div>
</section>

<footer class="site-footer abs">
  <h4>CORVEL NETWORKS</h4>
  <p class="address">PO Box 4120, Harbourline Business Centre, Westmere, WA 6901 AUSTRALIA</p>
  <div class="contact-line">
    <span><svg width="14" height="14" viewBox="0 0 14 14"><path d="M3 1l3 3-2 2c1 2 2 3 4 4l2-2 3 3-2 2C6 13 1 8 1 3z" fill="#fff"/></svg>1300 555 018</span>
    <span><svg width="16" height="12" viewBox="0 0 16 12"><rect x="1" y="1" width="14" height="10" fill="none" stroke="#fff" stroke-width="1.4"/><path d="M1 1l7 6 7-6" fill="none" stroke="#fff" stroke-width="1.4"/></svg>peering@corvelnet.example</span>
  </div>
  <div class="social"><i></i><i></i><i></i></div>
</footer>

<div class="bottom-bar abs">
  <div class="brand"><span class="brand-mark"></span>Corvel Networks</div>
  <p class="copyright">© Copyright 2015. Corvel Networks. All rights reserved.</p>
</div>

</body>
</html>
```